ATM Website-Great Opportunity for Portability

Hey We need YOU to help us make our ATM (Automatic Teller Machine)Website!!) We are a million dollar business that will look great on your portfolio! Our Name is "CORNER CASH POINT"
Previous ATM business (now sold) was www.cashbrivo.com.au (site being pulled down so look at it fast!)
The winner will get the same package that we will giving to the winner of our other project! (worth over $9,000)
http://jobs.pixelvorn.com/job.aspx?id=4827
**we are making a series of sites/applications Winners will be solo invited to work on all upcoming projects of that catigory**
***we are also looking for Outstanding freelance guys to work with on all future projects***
Main Points!!
1: one main page (that is not a blog!)
2: Then the Theme!
3: I don't want it to look like a word-press
I.e like this guys Word press http://www.trasqueld.com/
See how he has one main page then the rest are WP Theme :)
Key points to the Home Page!
See attached pic for the menu's needed and the call now key.
Main page needs to have
1. Clean, uncluttered, and follow the feel of our LOGO (attached) Be creative but simplistic with the page. Round curves are good)
2. Large hero images of happy poeple in the community but not looking too stocky or contrived - natural smiles, natural expressions, With Image of OUR ATM on the page!
3. Easy navigation
4: (3 big buttons like on our competitors site
(http://www.brightfundpoint.com.au/) With the titles
(get an ATM (and beside it "for your business")
(Own an ATM (increase your investment Portfolio)
(Latest ATM (See an ATM in action)
For the Theme Page,
It must flow on from the main menu but have a bread crum trail on the page of all the sub links somewhere on the left of the page (or somewhere else that might look better.
Theme page should have a Call now or email now option!! If you can fit in 2 without it looking cluttered that would be good.
I will attach our brochures so you can get a feel of our product.
Also you should be able to extract images from our brochure using GLEMBRA DOC TOOL or similar PDF editor if needed!!
logo attached and also found at www.cornercashpoint.com.au
Good Fonts to use!
Helvetica Neue LT (bold thin ect)
Helvetica Neue LT Com
Target Market(s)
Business Owners and Investors
Industry/Entity Type
Investment
Requirements
Must have
- The Call now Features in the attached file, Clean layout
Should not have
- Should not look like stock photo's and a cheap website or a template...

```html
<!DOCTYPE html>
<html lang="en">
<head>
<meta charset="utf-8">
<title>Corner Cash Point – Home</title>
<link rel="stylesheet" href="https://fonts.googleapis.com/css2?family=Arimo:wght@400;700&family=Roboto+Condensed:wght@300;400;700&display=swap">
<style>
:root{
  --green:#8cc63f;
  --green-dark:#0b6b0b;
  --green-deep:#0a5a0a;
  --text:#222;
  --muted:#555;
  --line:#d6d6d6;
  --panel:#ececec;
  --footer:#e9e9e9;
}
*{margin:0;padding:0;box-sizing:border-box}
html,body{width:1200px;height:1122px;overflow:hidden}
body{position:relative;background:#fff;font-family:Arimo,Helvetica,Arial,sans-serif;color:var(--text)}
.abs{position:absolute}
.cond{font-family:"Roboto Condensed",Arial,sans-serif}

.header-frame{left:0;top:0;width:1200px;height:497px;border-left:1px solid #ccc;border-bottom:1px solid #ccc;box-shadow:0 2px 3px rgba(0,0,0,.08)}

.brand{left:169px;top:24px;display:flex;align-items:center;gap:10px}
.brand-dot{width:46px;height:46px;border-radius:50%;background:var(--green)}
.brand-name{font-family:"Roboto Condensed",Arial,sans-serif;font-weight:700;font-size:17px;color:var(--green);line-height:1.1;width:90px}

.share{left:854px;top:14px;display:flex;align-items:center;gap:9px;font-size:11px;font-weight:700;padding-bottom:6px;border-bottom:1px solid #333;width:177px}
.social{font-size:10px;font-weight:700;color:#333}

.help{left:776px;top:62px;display:flex;gap:12px;align-items:flex-start}
.help-title{font-size:18px;color:#333;line-height:1.1}
.help-phone{font-size:23px;color:var(--green);line-height:1.2}
.help-phone b{font-weight:700}

.nav{left:150px;top:131px;width:900px;height:38px;border-radius:3px;background:linear-gradient(#dcdcdc,#a9a9a9);display:flex;overflow:hidden}
.nav a{font-size:13px;color:#222;text-decoration:none;line-height:38px;padding:0 12.5px}
.nav a.active{background:linear-gradient(#a6d86a,#5da82a);padding:0 17px}

.atm-visual{left:167px;top:202px;width:142px;height:295px;border-radius:10px 30px 4px 4px;background:linear-gradient(180deg,#4aa83a 0%,#2e8a2a 70%,rgba(255,255,255,0) 100%)}

.hero-title{left:336px;top:201px;font-size:24px;color:var(--green);line-height:29px}
.hero-title b{font-weight:700;letter-spacing:.5px}
.hero-list{left:336px;top:268px;width:410px;font-size:10.5px;line-height:17px;color:#222}
.hero-list p{margin-bottom:11px}

.btn{border-radius:3px;background:linear-gradient(#2e9a2e,#0a5e0a);border:1px solid #054705;color:#fff;font-size:17px;text-align:center}
.read-more{left:351px;top:433px;width:112px;height:38px;line-height:36px}

.contact{left:759px;top:207px;width:282px;height:263px;border-radius:4px;background:linear-gradient(#f6f6f6,#e2e2e2)}
.contact-tab{left:830px;top:202px;width:140px;height:14px;background:var(--green-dark);border-radius:3px 3px 0 0}
.contact h3{position:absolute;left:18px;top:22px;font-weight:400;font-size:17px;color:var(--green-dark);width:244px;display:flex;align-items:center;gap:10px}
.contact h3::after{content:"";flex:1;border-bottom:1px solid #333;margin-top:6px}
.contact p{position:absolute;left:18px;top:58px;width:240px;font-size:10.5px;line-height:17px;color:#333}
.field{position:absolute;left:47px;width:188px;height:19px;border:1px solid var(--green-dark);background:#fff;font-size:10.5px;color:#888;padding:2px 8px;line-height:14px}
.send{left:830px;top:393px;width:141px;height:32px;line-height:30px;font-size:16px}
.contact-base{left:806px;top:431px}

.crumbs{left:150px;top:516px;width:900px;height:28px;border:1px solid #c8c8c8;border-radius:3px;background:#ebebeb;overflow:hidden}
.crumbs span{position:absolute;left:0;top:0;width:112px;height:28px;background:var(--green);color:#fff;font-family:"Roboto Condensed",Arial,sans-serif;font-size:13px;text-align:center;line-height:28px}
.crumbs span::after{content:"";position:absolute;right:0;top:9px;border:5px solid transparent;border-right-color:#ebebeb}

.tile{top:572px;width:281px;height:187px;border-radius:3px;overflow:hidden;color:#fff}
.tile h2{position:absolute;left:18px;top:13px;font-family:"Roboto Condensed",Arial,sans-serif;font-weight:400;font-size:22px;text-shadow:0 1px 3px rgba(0,0,0,.6)}
.tile .tag{position:absolute;left:0;right:0;bottom:0;height:37px;background:rgba(40,40,40,.55);text-align:right;padding-right:18px;line-height:37px;font-family:"Roboto Condensed",Arial,sans-serif;font-size:15px}
.tile-1{left:159px;background:linear-gradient(135deg,#9a6a48,#d7a98a 50%,#6a4a3a)}
.tile-2{left:459px;background:linear-gradient(180deg,#b86a3a,#9a9a9a 45%,#5a5a5a)}
.tile-3{left:759px;background:linear-gradient(135deg,#444,#b08a60 55%,#6a6a6a)}

.welcome{left:169px;top:781px;font-size:23px;color:#222}
.welcome b{font-family:Arimo,Arial,sans-serif;font-weight:700;color:var(--green);font-size:22px;letter-spacing:.5px}
.about{left:168px;top:827px;width:555px;font-size:10.5px;line-height:17px;color:#222}
.about p{margin-bottom:6px}
.divider{left:750px;top:788px;height:173px;border-left:1px solid var(--green-dark)}

.media-head{left:777px;top:783px;width:259px;font-size:17px;color:#222;display:flex;align-items:center;gap:6px}
.media-head::after{content:"";flex:1;border-bottom:1px solid #333;margin-top:8px}
.news{left:777px;width:264px;padding-left:19px;padding-bottom:10px;border-bottom:1px dotted var(--green-dark)}
.news::before{content:"";position:absolute;left:2px;top:4px;border:4px solid transparent;border-left:6px solid var(--green)}
.news .date{font-size:10px;color:#222;line-height:14px}
.news .head{font-size:11px;font-weight:700;color:var(--green-dark);line-height:17px}

.footer{left:0;top:989px;width:1200px;height:133px;background:var(--footer);border-top:1px solid #d0d0d0}
.foot-nav{left:169px;top:1006px;font-size:11px;color:#222}
.foot-nav .sep{margin:0 5px}
.foot-nav .hl{color:var(--green)}
.copy{left:169px;top:1030px;font-size:9.5px;color:#222}
.copy span{color:var(--green)}
.link-us{left:169px;top:1056px;font-size:11px;display:flex;gap:10px;align-items:center}
.foot-brand{left:946px;top:1010px;display:flex;flex-direction:column;align-items:center;gap:5px}
.foot-brand i{width:54px;height:54px;border-radius:50%;background:#b9b9b9}
.foot-brand span{font-family:"Roboto Condensed",Arial,sans-serif;font-weight:700;font-size:10px;color:#a0a0a0}
</style>
</head>
<body>
<div class="abs header-frame"></div>

<div class="abs brand"><i class="brand-dot"></i><span class="brand-name">CORNER CASH POINT</span></div>

<div class="abs share"><span>Share Us:</span><span class="social">Pagenest</span><span class="social">Chirpline</span><span class="social">Clipstream</span></div>

<div class="abs help">
  <svg width="46" height="50" viewBox="0 0 46 50" aria-hidden="true">
    <path d="M9 6c3-2 6-1 7 2l3 7c1 2 0 4-2 5l-3 2c2 6 6 11 12 14l2-3c1-2 3-2 5-1l7 4c2 1 3 4 1 6l-3 4c-3 3-8 3-12 0C15 38 7 28 5 18 4 12 5 9 9 6z" fill="var(--green)"/>
    <path d="M26 4a16 16 0 0 1 15 15M26 10a10 10 0 0 1 9 9" stroke="var(--green)" stroke-width="2" fill="none"/>
    <ellipse cx="24" cy="47" rx="20" ry="2.5" fill="#ddd"/>
  </svg>
  <div class="cond">
    <div class="help-title">Need Help?</div>
    <div class="help-phone">Call on: <b>1300 482 917</b></div>
  </div>
</div>

<nav class="abs nav">
  <a class="active" href="#">Home</a><a href="#">About</a><a href="#">Investors</a><a href="#">Products &amp; Services</a><a href="#">Get a Free ATM</a><a href="#">Giving Back</a><a href="#">Who has One</a><a href="#">Media</a><a href="#">Career</a>
</nav>

<div class="abs atm-visual" role="img" aria-label="Green branded ATM machine"></div>

<h1 class="abs hero-title cond" style="font-weight:400">THE <b>5 BIG OPPORTUNITIES</b><br>YOU ARE MISSING</h1>
<div class="abs hero-list">
  <p>ATMs can increase foot traffic by 30%.*</p>
  <p>70% of people that used an ATM in an outlet then purchased a product in store.*</p>
  <p>8%-14% average increase in retail sales.**</p>
  <p>If your competitors don't have an ATM on site already, they soon will.</p>
  <p>ATMs in Australia currently process over 70 million cash transactions valued in excess of $13 billion every month.</p>
</div>
<div class="abs btn read-more">Read More</div>

<div class="abs contact-tab"></div>
<div class="abs contact">
  <h3 class="cond">Get in Thouch</h3>
  <p>Lorem Ipsum is simply dummy text of the printing and typesetting industry.</p>
  <div class="field" style="top:97px">Name</div>
  <div class="field" style="top:125px">Email Id</div>
  <div class="field" style="top:153px">Phone</div>
</div>
<div class="abs btn send">Get In Touch</div>
<svg class="abs contact-base" width="188" height="44" viewBox="0 0 188 44" aria-hidden="true">
  <defs><linearGradient id="baseG" x1="0" y1="0" x2="0" y2="1"><stop offset="0" stop-color="#3aa83a"/><stop offset="1" stop-color="#0a5e0a"/></linearGradient></defs>
  <path d="M0 19 L94 0 L188 19 L164 19 L164 40 Q164 43 161 43 L27 43 Q24 43 24 40 L24 19 Z" fill="url(#baseG)"/>
</svg>

<div class="abs crumbs"><span>Home</span></div>

<div class="abs tile tile-1" role="img" aria-label="Hands passing a bank card"><h2>Get an ATM</h2><div class="tag">For your Business</div></div>
<div class="abs tile tile-2" role="img" aria-label="People using a row of ATMs"><h2>Own an ATM</h2><div class="tag">Increase your investment Portfolio</div></div>
<div class="abs tile tile-3" role="img" aria-label="Hand taking cash from an ATM"><h2>Latest ATM</h2><div class="tag">See an ATM in action</div></div>

<h2 class="abs welcome cond" style="font-weight:400">Welcome to <b>CORNER CASH POINT</b></h2>
<div class="abs about">
  <p>Lorem Ipsum is simply dummy text of the printing and typesetting industry. Lorem Ipsum has been the industry's standard dummy text ever since the 1500s, when an unknown printer took a galley of type and scrambled it to make a type specimen book. It has survived not only five centuries, but also the leap into electronic typesetting, remaining essentially unchanged.</p>
  <p>It was popularised in the 1960s with the release of Letraset sheets containing Lorem Ipsum passages, and more recently with desktop publishing software like Aldus PageMaker including versions of Lorem Ipsum.</p>
</div>
<div class="abs divider"></div>

<h3 class="abs media-head cond" style="font-weight:400">Media</h3>
<div class="abs news" style="top:815px"><div class="date">16th Dec 2010</div><div class="head">Lorem Ipsum is simply dummy text of the printing and typesetting industry.</div></div>
<div class="abs news" style="top:897px"><div class="date">16th Dec 2010</div><div class="head">Lorem Ipsum is simply dummy text of the printing and typesetting industry.</div></div>

<footer class="abs footer"></footer>
<div class="abs foot-nav">Home<span class="sep">|</span>About<span class="sep">|</span>Investors<span class="sep">|</span>Products &amp; Services<span class="sep">|</span><span class="hl">Get a Free ATM</span><span class="sep">|</span>Giving Back<span class="sep">|</span>Who has One<span class="sep">|</span>Media<span class="sep">|</span>Career</div>
<div class="abs copy">© 2010 <span>Corner Cash Point</span>. All Rights Reserved.</div>
<div class="abs link-us"><span>Link Us:</span><span class="social">Pagenest</span><span class="social">Chirpline</span><span class="social">Clipstream</span></div>
<div class="abs foot-brand"><i></i><span>CORNER CASH POINT</span></div>
</body>
</html>
```